Postcard Design

Income tax servicesOver 20 years experienceBusiness and Personal Tax ReturnsAll State ReturnsFree Electronic FilingI would like a simple map showing how to get to my house.reasons to use a tax preparerYou don’t have to keep up with the many tax law changes or understand complicated tax law.Your time is worth money – add up the hours you would spend doing it yourself and calculate what that’s worth.A tax program in a box cannot represent you in an audit.A tax professional can answer your questions to help you make smarter tax-saving decisions.It gives you peace of mind knowing that a professional is taking care of it.It can save you money – if your tax preparer finds even one significant deduction or tax credit you may have missed, it can easily cover the cost to have them prepared.Going to be targeting the area within 2 square miles of my home office so would like to promote proximity to the possible clients

```html
<!DOCTYPE html>
<html lang="en">
<head>
<meta charset="utf-8">
<title>Income Tax Services Postcard</title>
<link href="https://fonts.googleapis.com/css2?family=Open+Sans:wght@400;600;700&family=Lato:wght@400;700&family=Roboto+Condensed:wght@400;700&display=swap" rel="stylesheet">
<style>
  :root {
    --bg: #e4e4e2;
    --maroon: #8c1414;
    --maroon-band: rgba(140, 26, 26, 0.82);
    --black: #1b1b1b;
    --yellow: #ffd400;
    --white: #ffffff;
    --ink: #222222;
    --muted: #555555;
    --line: #b9b9b9;
  }
  * { box-sizing: border-box; margin: 0; padding: 0; }
  html, body { width: 902px; height: 1200px; overflow: hidden; }
  body { background: var(--bg); font-family: "Lato", sans-serif; position: relative; }

  .card {
    position: absolute; left: 115px; width: 672px; height: 483px;
    background: var(--white); overflow: hidden;
    box-shadow: 0 6px 18px rgba(0,0,0,0.28);
  }
  .card-front { top: 60px; }
  .card-back { top: 640px; }

  /* FRONT */
  .front-photo {
    position: absolute; left: 0; top: 0; width: 672px; height: 380px;
    background: linear-gradient(160deg, #e9e2d6 0%, #d8ccb8 45%, #cfc9c0 75%, #e8e8e8 100%);
  }
  .front-title-band {
    position: absolute; left: 0; top: 0; width: 100%; height: 62px;
    background: var(--maroon-band);
    display: flex; align-items: center; justify-content: center;
  }
  .front-title {
    font-family: "Open Sans", sans-serif; font-weight: 700; font-size: 28px;
    color: var(--white); letter-spacing: 0.2px;
  }
  .front-wave { position: absolute; left: 0; top: 0; width: 672px; height: 483px; }

  .experience-badge { position: absolute; left: 18px; top: 188px; width: 170px; height: 170px; }
  .experience-badge svg { position: absolute; inset: 0; }
  .experience-text {
    position: absolute; inset: 0; display: flex; flex-direction: column;
    align-items: center; justify-content: center;
    font-family: "Roboto Condensed", sans-serif; color: var(--maroon); line-height: 1;
  }
  .experience-text .small { font-size: 21px; }
  .experience-text .big { font-size: 35px; font-weight: 700; margin: 3px 0; }

  .service-ribbon { position: absolute; left: 483px; top: 100px; width: 189px; height: 300px; }
  .service-label {
    position: absolute; left: 548px; top: 186px; width: 128px; height: 25px;
    background: var(--maroon); color: var(--white); border-radius: 13px 0 0 13px;
    font-family: "Open Sans", sans-serif; font-weight: 700; font-size: 16px;
    display: flex; align-items: center; justify-content: center;
  }
  .service-list {
    position: absolute; right: 14px; top: 230px; list-style: none; text-align: right;
    font-family: "Roboto Condensed", sans-serif; font-size: 16px; color: var(--ink);
  }
  .service-list li { line-height: 19px; margin-bottom: 11px; }
  .service-list li::after, .service-list li.two-line span::after {
    content: ""; display: inline-block; width: 7px; height: 7px; border-radius: 50%;
    background: var(--ink); margin-left: 6px; vertical-align: 2px;
  }
  .service-list li.two-line::after { display: none; }

  .brand { position: absolute; left: 508px; top: 398px; width: 150px; text-align: center; }
  .brand-name { font-family: "Open Sans", sans-serif; font-weight: 700; font-size: 17px; color: var(--ink); display: flex; align-items: center; justify-content: center; gap: 5px; }
  .brand-name::before { content: ""; width: 9px; height: 9px; border-radius: 50%; background: var(--ink); }
  .brand-tagline { font-family: "Open Sans", sans-serif; font-size: 6.5px; color: var(--muted); margin-top: 3px; }

  .call-now {
    position: absolute; display: flex; gap: 18px; white-space: nowrap;
    font-family: "Open Sans", sans-serif; font-weight: 700; font-size: 20px; color: var(--black);
  }
  .card-front .call-now { left: 38px; top: 410px; }
  .front-footer {
    position: absolute; left: 0; bottom: 0; width: 100%; height: 38px; background: var(--black);
    color: var(--white); font-family: "Open Sans", sans-serif; font-size: 14px; letter-spacing: 2px;
    display: flex; align-items: center; justify-content: center;
  }

  /* BACK */
  .back-panel {
    position: absolute; left: 0; top: 0; width: 352px; height: 483px;
    background: linear-gradient(180deg, #ffffff 40%, #e9e9e9 100%);
  }
  .back-photo {
    position: absolute; left: 0; top: 0; width: 352px; height: 180px;
    background: linear-gradient(135deg, #cfd3d6 0%, #e7dfc7 45%, #b9bec3 100%);
    clip-path: path("M0,0 H352 V150 C260,175 160,190 0,170 Z");
  }
  .yellow-curve { position: absolute; left: 0; top: 0; width: 372px; height: 483px; }
  .divider-stripe { position: absolute; left: 352px; top: 0; width: 12px; height: 483px; background: var(--maroon); }
  .map-disc {
    position: absolute; left: 258px; top: 92px; width: 128px; height: 128px; border-radius: 50%;
    border: 6px solid var(--yellow); background: radial-gradient(circle, #e2e0dc 0%, #cdcac5 100%);
    display: flex; align-items: center; justify-content: center;
  }
  .reasons-title {
    position: absolute; left: 22px; top: 210px; font-family: "Roboto Condensed", sans-serif;
    font-weight: 400; font-size: 16px; color: var(--ink); text-transform: uppercase;
  }
  .reasons-list { position: absolute; left: 22px; top: 236px; width: 320px; list-style: none; }
  .reasons-list li {
    position: relative; padding-left: 16px; font-size: 10.5px; line-height: 13px;
    color: var(--ink); margin-bottom: 5px;
  }
  .reasons-list li::before {
    content: ""; position: absolute; left: 0; top: 2px; width: 9px; height: 9px;
    border-radius: 50%; background: var(--maroon);
  }
  .back-bar { position: absolute; left: 0; bottom: 0; width: 364px; height: 56px; background: var(--black); }
  .back-bar .call-now { left: 28px; top: 13px; color: var(--white); }
  .stamp-box { position: absolute; left: 598px; top: 42px; width: 66px; height: 66px; border: 1.5px solid #444; }
  .address-line { position: absolute; left: 436px; width: 232px; height: 1px; background: var(--line); }
</style>
</head>
<body>

<section class="card card-front" aria-label="Postcard front">
  <div class="front-photo" role="img" aria-label="Photo of wooden letter stamps spelling tax refund on tax forms with a yellow binder clip"></div>
  <svg class="front-wave" viewBox="0 0 672 483" aria-hidden="true">
    <path d="M0,182 C120,290 230,350 370,318 C480,292 570,180 672,92 L672,483 L0,483 Z" fill="#1b1b1b"/>
    <path d="M0,192 C120,300 230,358 370,326 C480,300 570,188 672,100 L672,483 L0,483 Z" fill="#8c1414"/>
    <path d="M0,210 C120,318 230,374 370,342 C480,316 570,205 672,118 L672,483 L0,483 Z" fill="#ffffff"/>
  </svg>
  <header class="front-title-band"><h1 class="front-title">Income tax services</h1></header>

  <div class="experience-badge">
    <svg viewBox="0 0 160 160" aria-hidden="true">
      <polygon fill="#ffd400" stroke="#f0a800" stroke-width="2" points="160,80 146.7,93.3 153.9,110.6 136.5,117.8 136.6,136.6 117.8,136.5 110.6,153.9 93.3,146.7 80,160 66.7,146.7 49.4,153.9 42.2,136.5 23.4,136.6 22.2,117.8 6.1,110.6 13.3,93.3 0,80 13.3,66.7 6.1,49.4 22.2,42.2 23.4,23.4 42.2,22.2 49.4,6.1 66.7,13.3 80,0 93.3,13.3 110.6,6.1 117.8,22.2 136.6,23.4 136.5,42.2 153.9,49.4 146.7,66.7"/>
    </svg>
    <div class="experience-text">
      <span class="small">OVER</span>
      <span class="big">20 YEARS</span>
      <span class="small">EXPERIENCE</span>
    </div>
  </div>

  <svg class="service-ribbon" viewBox="0 0 189 300" aria-hidden="true">
    <defs>
      <linearGradient id="ribbonFill" x1="0" y1="0" x2="0" y2="1">
        <stop offset="0" stop-color="#ffd400"/>
        <stop offset="1" stop-color="#ffe23a"/>
      </linearGradient>
    </defs>
    <polygon points="0,148 189,0 189,300 94,240 0,300" fill="url(#ribbonFill)"/>
  </svg>
  <div class="service-label">MY SERVICE</div>
  <ul class="service-list">
    <li class="two-line"><span>Business and Personal</span><br>Tax Returns&nbsp;&nbsp;&nbsp;</li>
    <li>All State Returns</li>
    <li>Free Electronic Filing</li>
  </ul>

  <div class="brand">
    <div class="brand-name">Ledgerline</div>
    <div class="brand-tagline">Ledgerline. Careful Work Every Season.</div>
  </div>

  <div class="call-now"><span class="call-label">Call Now:</span><span class="call-number">0147258369</span></div>
  <footer class="front-footer">www.northfieldtaxdesk.com</footer>
</section>

<section class="card card-back" aria-label="Postcard back">
  <div class="back-panel"></div>
  <div class="back-photo" role="img" aria-label="Photo of a couple meeting with a tax adviser to review documents"></div>
  <svg class="yellow-curve" viewBox="0 0 372 483" aria-hidden="true">
    <path d="M330,0 C350,30 352,70 346,110" fill="none" stroke="#ffd400" stroke-width="4"/>
  </svg>
  <div class="divider-stripe"></div>
  <div class="map-disc" role="img" aria-label="Simple street map showing the home office location">
    <svg width="20" height="28" viewBox="0 0 20 28" aria-hidden="true">
      <path d="M10,0 C4.5,0 0,4.3 0,9.7 C0,17 10,28 10,28 C10,28 20,17 20,9.7 C20,4.3 15.5,0 10,0 Z" fill="#8c1414"/>
      <circle cx="10" cy="9.5" r="3.5" fill="#e2e0dc"/>
    </svg>
  </div>

  <h2 class="reasons-title">Reasons to use a tax preparer</h2>
  <ul class="reasons-list">
    <li>Your time is worth money – add up the hours you would spend doing it yourself and calculate what that’s worth.</li>
    <li>A tax program in a box cannot represent you in an audit.</li>
    <li>A tax professional can answer your questions to help you make smarter tax-saving decisions.</li>
    <li>It gives you peace of mind knowing that a professional is taking care of it.</li>
    <li>It can save you money – if your tax preparer finds even one significant deduction or tax credit you may have missed, it can easily cover the cost to have them prepared.</li>
    <li>Going to be targeting the area within 2 square miles of my home office so would like to promote proximity to the possible clients</li>
  </ul>

  <div class="back-bar"><div class="call-now"><span class="call-label">Call Now:</span><span class="call-number">0147258369</span></div></div>

  <div class="stamp-box"></div>
  <div class="address-line" style="top:232px"></div>
  <div class="address-line" style="top:270px"></div>
  <div class="address-line" style="top:308px"></div>
</section>

</body>
</html>
```